Fahrzeugbeschriftung für Vertrieb von chemischen Produkte wie z. B. Kühlschmierstoffe, Reiniger usw.
Zielgruppe
Wir sind in der metallverarbeitenden Industrie Zuhause. Wir vertreiben chemische Produkte wie z.B. Kühlschmierstoffe, Reiniger und Korrosionsschutzprodukte und betreuen unsere Kunden im Rahmen eines innovativen Fluidmanagements.
Unsere Zielgruppe sind Werkleiter, Produktionsleiter, Instandhalter und Einkäufer
Aufgabenstellung
Wir haben ein sehr umfangreiches Produkt- und Dienstleistungsportfolio was die Sache nicht unbedingt einfach macht.
- Zwecks Wiedererkennung hätten wir gerne unser Logo schön groß. Es kann der Schriftzug oder das Logo verwendet werden. Siehe Anhang
- Das 'VT' darf gerne auch übergroß sein
- Es sollten nur Farben verwendet werden die wir auch in unserem Print und WEB verwenden. Jeder unserer 5 Geschäftsbereiche hat seine eigene Farbe. Siehe www.vt-kalorex.de Eine Mischung bzw. ein fliesender Übergang von den Blau und Grün tönen könnten wir uns gut vorstellen.
- Auf der Startseite ist bei den einblendenden Bildern eine Wortwolke, die ebenfalls als Anregung genutzt werden darf.
- Das beschriftete Fahrzeug (Halvard Kombo in Silber)wird für Serviceeinsätze im Fluidmanagement verwendet.
- Folgenden Text sollte untergebracht werden: SYSTEMPARTNER FÜR DIE BEREICHE
KÜHLSCHMIERSTOFFE • REINIGer • KORROSIONSSCHUTZ • FILTRATION • PROZESSWASSER • FLUIDMANAGEMENT
- Angefügte Bilder können verwendet werden oder auch nicht
Unsere Servicebusse haben wir schon designenlassen --> Siehe Anhang 'HK Kombo'
Im ersten Step werden 5 Lunaras beschriftet. weitere sollen folgen

```html
<!DOCTYPE html>
<html lang="de">
<head>
<meta charset="utf-8">
<title>VT-KALOREX Fahrzeugbeschriftung – Alternativen</title>
<link href="https://fonts.googleapis.com/css2?family=Arimo:wght@700&family=Saira+Condensed:wght@600&family=Courgette&display=swap" rel="stylesheet">
<style>
  :root{
    --page:#ffffff;
    --ink:#000000;
    --navy:#0f2240;
    --blue:#2f8fd0;
    --teal:#3a9ea0;
    --green:#6aa84f;
    --silver:#d9dde2;
    --silver-light:#eef0f2;
    --silver-dark:#9aa1a8;
    --panel:#e7ebee;
    --white:#ffffff;
  }
  *{margin:0;padding:0;box-sizing:border-box}
  html,body{width:1200px;height:1200px;overflow:hidden;background:var(--page)}
  .canvas{position:relative;width:1200px;height:1200px}
  .alt-label{
    position:absolute;left:86px;
    font-family:"Arimo",Arial,sans-serif;font-weight:700;font-size:24px;color:var(--ink);
  }
  .alt-label--one{top:136px}
  .alt-label--two{top:683px}
  .wrap-panel{position:absolute;left:86px;width:1028px;height:300px}
  .wrap-panel--one{top:200px}
  .wrap-panel--two{top:747px}
  .company-name{font-family:"Saira Condensed","Arial Narrow",sans-serif;font-weight:600;font-size:80px;fill:var(--navy)}
  .claim{font-family:"Courgette",cursive;font-size:17px;fill:var(--white)}
  .service-list{font-family:"Saira Condensed","Arial Narrow",sans-serif;font-weight:600;font-size:15px;fill:var(--navy);letter-spacing:.3px}
  .web-address{font-family:"Saira Condensed","Arial Narrow",sans-serif;font-weight:600;font-size:14px;fill:var(--white)}
</style>
</head>
<body>
<main class="canvas">

  <h2 class="alt-label alt-label--one">Alternative-1</h2>
  <svg class="wrap-panel wrap-panel--one" viewBox="0 0 1028 300" xmlns="http://www.w3.org/2000/svg">
    <defs>
      <linearGradient id="bodySilver1" x1="0" y1="0" x2="0" y2="1">
        <stop offset="0" stop-color="var(--silver-light)"/><stop offset="1" stop-color="var(--silver)"/>
      </linearGradient>
      <linearGradient id="dotField1" x1="0" y1="0" x2="1" y2="0">
        <stop offset="0" stop-color="var(--blue)" stop-opacity=".55"/>
        <stop offset=".55" stop-color="var(--green)" stop-opacity=".35"/>
        <stop offset="1" stop-color="var(--green)" stop-opacity="0"/>
      </linearGradient>
      <linearGradient id="headerStrip1" x1="0" y1="0" x2="1" y2="0">
        <stop offset="0" stop-color="var(--blue)"/><stop offset=".5" stop-color="var(--teal)"/><stop offset="1" stop-color="var(--green)"/>
      </linearGradient>
      <linearGradient id="sillBand1" x1="0" y1="0" x2="1" y2="0">
        <stop offset="0" stop-color="var(--silver-dark)" stop-opacity="0"/>
        <stop offset=".5" stop-color="var(--silver-dark)" stop-opacity=".6"/>
        <stop offset="1" stop-color="var(--teal)" stop-opacity=".5"/>
      </linearGradient>
    </defs>
    <rect class="body-surface" x="0" y="0" width="1028" height="300" rx="18" fill="url(#bodySilver1)"/>
    <rect x="0" y="0" width="400" height="300" rx="18" fill="url(#dotField1)" role="img" aria-label="Rasterpunktfläche in Blau und Grün"/>
    <rect x="280" y="250" width="520" height="34" fill="url(#sillBand1)" role="img" aria-label="Rasterpunktband in Grau"/>
    <text class="company-name" x="70" y="168">VT-KALOREX</text>
    <g class="service-panel">
      <rect x="560" y="60" width="400" height="210" rx="10" fill="var(--panel)"/>
      <rect x="560" y="60" width="400" height="36" rx="10" fill="url(#headerStrip1)"/>
      <text class="claim" x="580" y="84">Systempartner Für Die Bereiche</text>
      <text class="service-list" x="590" y="124">• KÜHLSCHMIERSTOFFE</text>
      <text class="service-list" x="590" y="146">• REINIGER</text>
      <text class="service-list" x="590" y="168">• KORROSIONSSCHUTZ</text>
      <text class="service-list" x="590" y="190">• FILTRATION</text>
      <text class="service-list" x="590" y="212">• PROZESSWASSER</text>
      <text class="service-list" x="590" y="234">• FLUIDMANAGEMENT</text>
      <rect x="790" y="152" width="150" height="34" rx="6" fill="var(--green)"/>
      <text class="web-address" x="865" y="174" text-anchor="middle">WWW.VT-KALOREX.DE</text>
    </g>
  </svg>

  <h2 class="alt-label alt-label--two">Alternative-2</h2>
  <svg class="wrap-panel wrap-panel--two" viewBox="0 0 1028 300" xmlns="http://www.w3.org/2000/svg">
    <defs>
      <linearGradient id="bodySilver2" x1="0" y1="0" x2="0" y2="1">
        <stop offset="0" stop-color="var(--silver-light)"/><stop offset="1" stop-color="var(--silver)"/>
      </linearGradient>
      <linearGradient id="dotField2" x1="0" y1="0" x2="1" y2="0">
        <stop offset="0" stop-color="var(--blue)" stop-opacity=".55"/>
        <stop offset=".55" stop-color="var(--green)" stop-opacity=".35"/>
        <stop offset="1" stop-color="var(--green)" stop-opacity="0"/>
      </linearGradient>
      <linearGradient id="fluidPhoto2" x1="0" y1="0" x2="1" y2="1">
        <stop offset="0" stop-color="#7d8790"/><stop offset=".5" stop-color="#dfe5ea"/><stop offset="1" stop-color="#9fb3c2"/>
      </linearGradient>
      <linearGradient id="headerStrip2" x1="0" y1="0" x2="1" y2="0">
        <stop offset="0" stop-color="var(--blue)"/><stop offset=".5" stop-color="var(--teal)"/><stop offset="1" stop-color="var(--green)"/>
      </linearGradient>
    </defs>
    <rect class="body-surface" x="0" y="0" width="1028" height="300" rx="18" fill="url(#bodySilver2)"/>
    <rect x="280" y="0" width="450" height="290" fill="url(#fluidPhoto2)" opacity=".85" role="img" aria-label="Foto: Kühlschmierstoff spritzt auf Metallbearbeitung"/>
    <rect x="0" y="0" width="400" height="300" rx="18" fill="url(#dotField2)" role="img" aria-label="Rasterpunktfläche in Blau und Grün"/>
    <text class="company-name" x="70" y="168">VT-KALOREX</text>
    <g class="service-panel">
      <rect x="560" y="60" width="400" height="210" rx="10" fill="var(--panel)" opacity=".9"/>
      <rect x="560" y="60" width="400" height="36" rx="10" fill="url(#headerStrip2)"/>
      <text class="claim" x="580" y="84">Systempartner Für Die Bereiche</text>
      <text class="service-list" x="590" y="124">• KÜHLSCHMIERSTOFFE</text>
      <text class="service-list" x="590" y="146">• REINIGER</text>
      <text class="service-list" x="590" y="168">• KORROSIONSSCHUTZ</text>
      <text class="service-list" x="590" y="190">• FILTRATION</text>
      <text class="service-list" x="590" y="212">• PROZESSWASSER</text>
      <text class="service-list" x="590" y="234">• FLUIDMANAGEMENT</text>
      <rect x="790" y="152" width="150" height="34" rx="6" fill="var(--green)"/>
      <text class="web-address" x="865" y="174" text-anchor="middle">WWW.VT-KALOREX.DE</text>
    </g>
  </svg>

</main>
</body>
</html>
```